Kereru Creative Harvest Fair

We are holding our inaugural event on the 21st October 2022 on the TerraStudia campus in Palmerston North., from 10am until 2pm.The event will be a mix of Fourth year Food Technology students presenting their student projects and local producers show casing and educating around their products. The event is bought to you by CropNest along with Ashcombe Vale District Council and BRIX. The overall plan is to bring a spotlight to the amount of research and food related businesses are on this side of the river. The event will be free to enter and there will be food and products to purchase, but the main focus is on education.

```html
<!DOCTYPE html>
<html lang="en">
<head>
<meta charset="utf-8">
<title>Kereru Creative Harvest Fair</title>
<link href="https://fonts.googleapis.com/css2?family=Montserrat:wght@500;700;800&family=Permanent+Marker&family=Tenor+Sans&display=swap" rel="stylesheet">
<style>
  :root {
    --page: #ffffff;
    --paper: #f5f5f3;
    --ink: #1a1a1a;
    --red: #d3291b;
    --yellow: #fcc537;
    --photo-sky: #8fb6d9;
    --photo-food: #c9a77a;
  }
  * { margin: 0; padding: 0; box-sizing: border-box; }
  html, body { width: 1071px; height: 1200px; overflow: hidden; background: var(--page); }
  .poster {
    position: absolute; left: 202px; top: 125px; width: 666px; height: 944px;
    background: var(--paper); overflow: hidden;
    font-family: "Montserrat", sans-serif; color: var(--ink);
  }
  .yellow-sweep { position: absolute; left: 0; top: 0; width: 666px; height: 944px; }
  .venue {
    position: absolute; top: 38px; width: 100%; text-align: center;
    font-family: "Tenor Sans", sans-serif; font-variant: small-caps; font-size: 19px; letter-spacing: 1px; line-height: 24px;
  }
  .year { position: absolute; top: 84px; width: 100%; text-align: center; font-weight: 700; font-size: 28px; line-height: 34px; }
  .date-row {
    position: absolute; top: 126px; left: 143px; width: 381px; height: 40px;
    display: flex; align-items: center;
    font-weight: 700; font-size: 27px;
  }
  .date-row .side {
    width: 155px; height: 36px; line-height: 33px; text-align: center;
    border-top: 2px solid var(--ink); border-bottom: 2px solid var(--ink);
  }
  .date-row .day { width: 71px; text-align: center; font-size: 50px; font-weight: 800; line-height: 40px; }
  .time { position: absolute; top: 178px; width: 100%; text-align: center; font-weight: 700; font-size: 28px; line-height: 34px; }
  .title {
    position: absolute; top: 232px; width: 100%; text-align: center;
    font-family: "Permanent Marker", cursive; font-weight: 400; color: var(--red); font-size: 90px; line-height: 118px;
  }
  .subtitle-bar {
    position: absolute; top: 358px; left: 95px; width: 470px; height: 30px;
    background: var(--yellow); border-radius: 4px 14px 6px 12px;
    display: flex; align-items: center; justify-content: center;
    font-weight: 700; font-size: 16px; letter-spacing: 1px;
  }
  .feature { position: absolute; top: 424px; width: 260px; text-align: center; }
  .feature.students { left: 67px; }
  .feature.producers { left: 327px; }
  .feature .photo {
    width: 208px; height: 208px; margin: 0 auto; border-radius: 30px;
    box-shadow: 0 6px 14px rgba(0,0,0,0.25);
  }
  .students .photo { background: linear-gradient(160deg, var(--photo-sky), #d7c2ae 70%, #5d6f8a); }
  .producers .photo { background: radial-gradient(circle at 50% 55%, #e77d4f, var(--photo-food) 45%, #5f8a3e 100%); }
  .feature .caption { margin-top: 22px; font-weight: 700; font-size: 16px; line-height: 20px; letter-spacing: 1px; }
  .notes {
    position: absolute; top: 730px; width: 100%; text-align: center; list-style: none;
    font-family: "Tenor Sans", sans-serif; font-size: 15px; letter-spacing: 1px; line-height: 25px;
  }
  .notes li::before { content: ""; display: inline-block; width: 7px; height: 7px; border-radius: 50%; background: var(--red); margin-right: 6px; vertical-align: 2px; }
  .partners { position: absolute; top: 808px; left: 0; width: 100%; height: 85px; background: var(--page); }
  .partners .credit { margin-top: 12px; text-align: center; font-family: "Tenor Sans", sans-serif; font-size: 10px; line-height: 14px; }
  .partner-names { display: flex; justify-content: center; gap: 80px; margin-top: 14px; }
  .partner-name { font-weight: 700; font-size: 26px; line-height: 34px; color: var(--ink); }
  .footer {
    position: absolute; top: 893px; left: 0; width: 100%; height: 51px; background: var(--yellow);
    display: flex; align-items: center; justify-content: space-between; padding: 0 36px;
  }
  .footer .web { color: var(--red); font-weight: 700; font-size: 13px; letter-spacing: 0.5px; }
  .footer .social { display: flex; gap: 14px; }
  .footer .social span { width: 20px; height: 20px; border-radius: 50%; background: var(--red); }
</style>
</head>
<body>
<main class="poster">
  <svg class="yellow-sweep" viewBox="0 0 666 944" aria-hidden="true">
    <polygon points="0,810 0,782 666,398 666,810" fill="#fcc537"/>
  </svg>

  <p class="venue">the TerraStudia campus in Palmerston North</p>
  <p class="year">2022</p>
  <p class="date-row"><span class="side">OCTOBER</span><span class="day">21</span><span class="side">FRIDAY</span></p>
  <p class="time">10AM-2PM</p>
  <h1 class="title">Food Festival</h1>
  <p class="subtitle-bar">EDUCATION AND FOOD EXHIBITION</p>

  <section class="feature students">
    <div class="photo" role="img" aria-label="Group of smiling students looking down at the camera against a blue sky"></div>
    <p class="caption">STUDENT PROJECTS</p>
  </section>
  <section class="feature producers">
    <div class="photo" role="img" aria-label="Tray of fresh local produce: salmon, avocado, cheese, tomatoes, olives and nuts"></div>
    <p class="caption">PRODUCTS ON LOCAL<br>PRODUCERS</p>
  </section>

  <ul class="notes">
    <li>ENTRANCE IS FREE OF CHARGE</li>
    <li>THERE WILL BE FOOD AND PRODUCTS TO PURCHASE</li>
  </ul>

  <section class="partners">
    <p class="credit">The event is brought to you by CropNest along with Ashcombe Vale District Council and BRIX.</p>
    <div class="partner-names">
      <span class="partner-name">CropNest</span>
      <span class="partner-name">ASHVALE</span>
    </div>
  </section>

  <footer class="footer">
    <span class="web">WWW.CROPNEST.COM</span>
    <div class="social" aria-hidden="true"><span></span><span></span><span></span></div>
  </footer>
</main>
</body>
</html>
```